Church Lanterns Over Millbrook Gospel Booklet Design

We need a booklet designed that we will be printing to hand out in our community. Wording for each page will be provided and we need graphic design to produce the layouts in a format ready for print. Booklet will be 4.75" x 4.75" square and a total of 12 pages: 1 cover page front, 1 cover page back, 10 inside pages some of which will be full spread across 2 pages.

Target Market(s)

English speaking Westerners

Industry/Entity Type

Religious

Font styles to use
Serif

Colors
ffffff
85abd2
0292cd
33b8a4
5c5c5c

Requirements
Must have
• Minimalist design with clean look described in attached document
Nice to have
• Aesthetically pleasing graphics, crisp fonts, excellent turn around times
Should not have
• Effeminate design, busy look with too much graphic and text

```html
<!DOCTYPE html>
<html lang="en">
<head>
<meta charset="utf-8">
<title>Lanterns Over Millbrook — Booklet Spreads</title>
<link href="https://fonts.googleapis.com/css2?family=Montserrat:wght@300;400;500;600;700;800&family=Oswald:wght@400;500&display=swap" rel="stylesheet">
<style>
  :root{
    --page-bg:#e3e3e3;
    --white:#ffffff;
    --sky:#85abd2;
    --blue:#0292cd;
    --teal:#33b8a4;
    --ink:#5c5c5c;
    --dark:#2a2a2a;
    --soft:#f1f1f1;
  }
  *{box-sizing:border-box;margin:0;padding:0}
  html,body{width:1200px;height:1200px;overflow:hidden}
  body{background:var(--page-bg);font-family:"Montserrat",sans-serif;color:var(--dark);position:relative}
  .spread{position:absolute;width:558px;height:280px;background:var(--white);box-shadow:0 6px 14px rgba(0,0,0,.12);overflow:hidden}
  .half{position:absolute;top:0;width:279px;height:280px}
  .half.left{left:0}.half.right{left:279px}
  .photo{position:absolute}
  .abs{position:absolute}
  .small{font-size:7.2px;line-height:16.5px;color:var(--dark);font-weight:400}
  .tiny{font-size:6.6px;line-height:15.5px;color:var(--dark)}
  .quote-mark{font-family:"Oswald",sans-serif;font-weight:500;font-size:20px;line-height:1;color:var(--dark);text-align:center}
  .center{text-align:center}
  .blue{color:var(--blue)}.teal{color:var(--teal)}
  .bar{position:absolute;height:12px}

  /* spread 1 */
  .s1{left:30px;top:161px}
  .cover-frame{position:absolute;left:20px;top:30px;width:240px;height:229px;border:1px solid var(--blue)}
  .cover-ghost{position:absolute;left:21px;top:31px;width:238px;height:227px;background:radial-gradient(ellipse at 45% 45%,#f2f2f2 0%,#fafafa 55%,#fff 100%)}
  .cover-photo{left:279px;top:0;width:279px;height:280px;background:radial-gradient(circle at 50% 80%,#ffe7a0 0%,#f0b04a 22%,#a9794a 48%,#5e4a3c 75%,#3e3530 100%)}
  .cover-lines{position:absolute;left:301px;top:30px;width:238px;height:229px;border:1px solid rgba(255,255,255,.7);border-top:none}
  .cover-title{position:absolute;left:279px;top:18px;width:279px;text-align:center;font-family:"Oswald",sans-serif;font-weight:500;font-size:21px;color:var(--white);letter-spacing:.2px}
  .cover-title span{background:transparent;padding:0 8px}
  .cover-rule{position:absolute;top:30px;height:1px;background:rgba(255,255,255,.8)}

  /* spread 2 */
  .s2{left:614px;top:158px}
</style>
</head>
<body>

<!-- Spread 1: cover -->
<section class="spread s1">
  <div class="cover-ghost" role="img" aria-label="Faint pale image of open hands holding a cross"></div>
  <div class="cover-frame"></div>
  <div class="photo cover-photo" role="img" aria-label="Silhouetted open hands raised toward a glowing sunset sky"></div>
  <div class="cover-lines"></div>
  <div class="cover-rule" style="left:301px;width:14px"></div>
  <div class="cover-rule" style="left:525px;width:14px"></div>
  <h1 class="cover-title">LANTERNS OVER MILLBROOK</h1>
</section>

<!-- Spread 2: creation -->
<section class="spread s2">
  <div class="photo" style="left:21px;top:21px;width:238px;height:238px;background:linear-gradient(180deg,#5b2b4a 0%,#c4463a 35%,#f39a3a 55%,#d86a3a 72%,#3a2422 88%,#1e1414 100%)" role="img" aria-label="Wooden cross on a hilltop against a fiery sunset"></div>
  <p class="abs small" style="left:299px;top:16px;width:245px;line-height:16px">God willingly created the universe, meaning he envisioned, designed, &amp; made us.</p>
  <div class="abs quote-mark" style="left:300px;top:84px;width:240px">&ldquo;</div>
  <p class="abs center" style="left:290px;top:106px;width:260px;font-size:17px;line-height:22px;font-weight:400;color:var(--dark)">In the beginning <b class="blue" style="font-weight:700">GOD</b><br>created the <b class="teal" style="font-weight:700">heavens &amp; the earth.</b></p>
  <div class="abs quote-mark" style="left:300px;top:178px;width:240px">&rdquo;</div>
  <div class="abs" style="left:356px;top:256px;width:42px;height:2px;background:var(--dark)"></div>
  <div class="abs" style="left:416px;top:255px;width:4px;height:4px;border-radius:50%;background:var(--blue)"></div>
  <div class="abs" style="left:438px;top:256px;width:42px;height:2px;background:var(--dark)"></div>
</section>

<!-- Spread 3: foundational truths -->
<section class="spread" style="left:30px;top:464px">
  <div class="photo" style="left:21px;top:21px;width:238px;height:86px;background:linear-gradient(180deg,#2c5fa8 0%,#6d9ad0 35%,#f7e08a 58%,#d6a43a 70%,#5c4a20 100%)" role="img" aria-label="Sun rising over a golden meadow with trees"></div>
  <p class="abs" style="left:21px;top:114px;width:250px;font-size:9.6px;line-height:12.5px;font-weight:600;color:var(--blue)">This reality establishes some foundational truths for all of us:</p>
  <ul class="abs" style="left:21px;top:145px;width:245px;list-style:none">
    <li style="position:relative;padding-left:12px;font-size:7px;line-height:9px;margin-bottom:11px"><span style="position:absolute;left:0;top:1px;width:6px;height:6px;border-radius:50%;background:var(--teal)"></span>God loves us - he didn't have to create us; we are here because he couldn't imagine life without us.</li>
    <li style="position:relative;padding-left:12px;font-size:7px;line-height:9px;margin-bottom:11px"><span style="position:absolute;left:0;top:1px;width:6px;height:6px;border-radius:50%;background:var(--teal)"></span>God is the proper authority in our lives - if he designed and made us, he rightfully owns us.</li>
    <li style="position:relative;padding-left:12px;font-size:7px;line-height:9px;margin-bottom:11px"><span style="position:absolute;left:0;top:1px;width:6px;height:6px;border-radius:50%;background:var(--teal)"></span>God knows the purpose of our lives - if he designed and made us, he knows why we are here.</li>
    <li style="position:relative;padding-left:12px;font-size:7px;line-height:9px"><span style="position:absolute;left:0;top:1px;width:6px;height:6px;border-radius:50%;background:var(--teal)"></span>God's truth is the truth we need - if he designed &amp; made us, he knows what it takes for life to go well for us.</li>
  </ul>
  <p class="abs small" style="left:300px;top:18px;width:240px;text-align:justify">But we, mankind, have all rejected God's authority in our lives. And because he rightfully owns us, our rebellion against God is a grave injustice; an act of treason for which we deserve to be cut off from God forever.</p>
  <div class="abs quote-mark" style="left:300px;top:116px;width:240px">&ldquo;</div>
  <p class="abs center" style="left:300px;top:133px;width:240px;font-size:12px;color:var(--dark)">For the</p>
  <p class="abs center" style="left:300px;top:147px;width:240px;font-size:20px;font-weight:700;color:var(--blue);letter-spacing:.5px">WAGES OF SIN</p>
  <p class="abs center" style="left:300px;top:171px;width:240px;font-size:26px;font-weight:300;color:var(--teal);letter-spacing:1px"><span style="font-size:12px;color:var(--dark)">is </span>DEATH<span style="color:var(--dark);font-weight:700">...</span></p>
  <p class="abs center" style="left:300px;top:203px;width:240px;font-size:7px;font-weight:700">(Romans 6:23)</p>
  <div class="abs quote-mark" style="left:300px;top:216px;width:240px">&rdquo;</div>
</section>

<!-- Spread 4: alienation -->
<section class="spread" style="left:614px;top:457px">
  <div class="half left" style="background:var(--soft)"></div>
  <div class="bar" style="left:20px;top:21px;width:62px;background:#4f7bb8"></div>
  <div class="bar" style="left:197px;top:247px;width:62px;background:#4f7bb8"></div>
  <p class="abs center" style="left:20px;top:55px;width:239px;font-size:8px;font-weight:700;color:#1e9a7a"><span style="display:inline-block;width:14px;height:1px;background:var(--dark);vertical-align:middle;margin-right:6px"></span>ALIENATION FROM GOD<span style="display:inline-block;width:14px;height:1px;background:var(--dark);vertical-align:middle;margin-left:6px"></span></p>
  <p class="abs small" style="left:35px;top:80px;width:210px;text-align:justify">This alienation from God is evident in a myriad of ways including poverty, crime, conflict in our relationships, and our internal struggles. But worse, when we die, we must face the consequences for our rejection of God by spending eternity in hell - a lake of fire created by God as the place where our treason is brought to justice.</p>
  <div class="bar" style="left:478px;top:21px;width:62px;background:var(--teal)"></div>
  <div class="bar" style="left:299px;top:247px;width:62px;background:var(--teal)"></div>
  <p class="abs small" style="left:299px;top:40px;width:240px;text-align:justify">But God does not want you to pay for your own sins. God loves us so much he sent his only son to save us. Jesus Christ died on the cross to serve our sentence for our rebellion against God and rose again on the third day. Since Christ paid our full penalty, we can be completely forgiven and reconciled to God</p>
  <div class="abs quote-mark" style="left:299px;top:140px;width:240px">&ldquo;</div>
  <p class="abs center tiny" style="left:305px;top:160px;width:228px;line-height:16px">For God so <b class="blue">loved the world</b> that he sent his <b class="blue">one</b><br><b class="teal">&amp; only son</b> that whosoever <b>believes in him</b> will<br>not perish but <b>HAVE ETERNAL LIFE.</b></p>
  <div class="abs quote-mark" style="left:299px;top:222px;width:240px">&rdquo;</div>
</section>

<!-- Spread 5: how to be saved -->
<section class="spread" style="left:28px;top:763px">
  <div class="photo" style="left:0;top:0;width:279px;height:160px;background:linear-gradient(180deg,#5e9ed8 0%,#bcd9f2 35%,#eef6fd 70%,#ffffff 100%)" role="img" aria-label="Radiant light breaking through clouds in a blue sky"></div>
  <p class="abs" style="left:20px;top:155px;width:245px;font-size:9.5px;font-weight:600;color:var(--teal)">Here is what you must do to be saved.</p>
  <p class="abs tiny" style="left:20px;top:174px;width:240px;line-height:15px;text-align:justify">First, ask Jesus Christ to save you (Since he is God, he can hear you); Acknowledge that God is the rightful authority of the universe and your life. Apologize to him for your rebellion against God. Ask Jesus Christ to come into your life as your Lord and Savior. This decision will immediately trigger his miracle of salvation in you. God now lives in you!</p>
  <p class="abs" style="left:299px;top:21px;font-size:7px;font-weight:600">If you confess with your mouth that</p>
  <p class="abs" style="left:298px;top:36px;font-size:33px;line-height:34px;font-weight:300;color:var(--blue);letter-spacing:1px">JESUS IS</p>
  <p class="abs" style="left:298px;top:68px;font-size:50px;line-height:50px;font-weight:400;color:var(--blue);letter-spacing:1px">LORD</p>
  <p class="abs" style="left:420px;top:123px;font-size:7px">&amp; believe in your heart</p>
  <p class="abs" style="left:299px;top:146px;font-size:12.5px;line-height:17px;color:var(--dark)">That God raised him<br>from the dead</p>
  <p class="abs" style="right:21px;top:190px;font-size:10px;text-align:right">You will be</p>
  <p class="abs" style="right:20px;top:202px;font-size:28px;font-weight:800;color:var(--teal);letter-spacing:1px">SAVED</p>
  <p class="abs" style="right:21px;top:244px;font-size:7px">Romans 10:9</p>
</section>

<!-- Spread 6: next steps -->
<section class="spread" style="left:611px;top:761px">
  <div class="photo" style="left:0;top:0;width:279px;height:170px;background:linear-gradient(180deg,#15202c 0%,#1f4f66 30%,#2f7e94 50%,#1d3342 72%,#8a8f93 90%,#ffffff 100%)" role="img" aria-label="Open Bible on a table lit by rays of blue light"></div>
  <p class="abs tiny" style="left:20px;top:185px;width:240px;text-align:justify">Next, God has given us the Bible and his church as the key tools for us to grow in our understanding of God and our personal relationship with him. So, it is essential you find a local church that believes the Bible is 100% true. Tell one of the pastors you are a brand new Christian and they will help you from there.</p>
  <div class="photo" style="left:279px;top:0;width:279px;height:280px;background:linear-gradient(180deg,#fbfbfb 0%,#f2ede8 22%,#c9c7cc 34%,#6c8fb8 46%,#2f5f9a 65%,#184a86 100%)" role="img" aria-label="Layered blue mountain ranges fading into morning haze"></div>
  <p class="abs center" style="left:279px;top:23px;width:279px;font-size:11.5px;color:var(--dark)">If you confess with your mouth that</p>
  <p class="abs center" style="left:279px;top:36px;width:279px;font-size:27px;line-height:30px;font-weight:700;color:#1c1c1c;letter-spacing:1px">JESUS IS LORD</p>
  <p class="abs center" style="left:279px;top:68px;width:279px;font-size:9.5px;line-height:12px;color:var(--dark)">and believe in your heart that God raised him<br>from the dead</p>
  <p class="abs center" style="left:279px;top:187px;width:279px;font-size:13.5px;font-weight:600;color:var(--white);letter-spacing:.5px">YOU WILL BE SAVED</p>
</section>

</body>
</html>
```